Cloud Based Internet Protection Service Business Cards

I would like a professionally designed business card. I already have a logo which I have attached.

The business is an online cloud based internet protection service aimed parents, particularly at non-technical parents and also schools.

The card should be be quite simple in its design, not to full of text and give its information in a clear and concise manner

Target Market(s)

Parents (especially non-technical parents) and also schools

Industry/Entity Type

Internet

Colors

Designer to choose colors to be used in the design.

Requirements
Should not have
• Too much text or be too cluttered. No decorative fonts, just a clear and concise font.

```html
<!DOCTYPE html>
<html lang="en">
<head>
<meta charset="utf-8">
<title>SafeNest Business Cards</title>
<link rel="stylesheet" href="https://fonts.googleapis.com/css2?family=Open+Sans:wght@400;600&family=Lobster&display=swap">
<style>
  :root {
    --stage: #4a0c0c;
    --charcoal: #333334;
    --signal-red: #ee4131;
    --paper: #ffffff;
    --fold: #9a9a9a;
    --ink: #3a3a3a;
    --rule: #e8e8e8;
  }
  * { margin: 0; padding: 0; box-sizing: border-box; }
  html, body { width: 1200px; height: 970px; overflow: hidden; }
  body {
    position: relative;
    background: var(--stage);
    font-family: "Open Sans", sans-serif;
  }
  .card {
    position: absolute;
    background: var(--charcoal);
    box-shadow: 0 10px 24px rgba(0,0,0,.45);
  }
  .card-front { left: 55px; top: 34px; width: 718px; height: 431px; }
  .card-back { left: 414px; top: 507px; width: 713px; height: 427px; }

  .red-band { position: absolute; top: 0; bottom: 0; background: var(--signal-red); }
  .card-front .red-band { left: 174px; width: 369px; }
  .card-back .red-band { left: 347px; right: 0; }

  .brand {
    position: absolute;
    display: flex;
    align-items: center;
    gap: 12px;
    color: var(--paper);
    font-weight: 600;
    letter-spacing: 2px;
    white-space: nowrap;
  }
  .brand-dot { width: 30px; height: 30px; border-radius: 50%; background: var(--paper); }
  .card-front .brand { left: 190px; top: 224px; width: 337px; justify-content: center; font-size: 46px; }
  .card-back .brand { left: 375px; top: 158px; width: 340px; justify-content: center; font-size: 44px; }

  .ribbon {
    position: absolute;
    background: var(--paper);
    box-shadow: 0 3px 4px rgba(0,0,0,.25);
    display: flex;
    align-items: center;
    justify-content: center;
    color: var(--ink);
  }
  .ribbon-fold { position: absolute; width: 0; height: 0; }
  .card-front .ribbon { left: 153px; top: 292px; width: 411px; height: 41px; font-size: 24px; }
  .card-front .fold-left { left: 153px; top: 333px; border-top: 14px solid var(--fold); border-left: 21px solid transparent; }
  .card-front .fold-right { left: 543px; top: 333px; border-top: 14px solid var(--fold); border-right: 21px solid transparent; }

  .card-back .ribbon { left: 326px; top: 240px; width: 387px; height: 40px; font-family: "Lobster", cursive; font-size: 34px; }
  .card-back .fold-left { left: 326px; top: 280px; border-top: 13px solid var(--fold); border-left: 21px solid transparent; }
  .designation { position: absolute; left: 347px; width: 322px; top: 290px; text-align: center; color: var(--paper); font-size: 12px; }

  .faint-mark {
    position: absolute; left: 40px; top: 80px; width: 270px; height: 200px;
    border-radius: 50%; background: rgba(255,255,255,.05);
  }
  .contact-list { position: absolute; left: 73px; top: 93px; width: 224px; list-style: none; color: var(--paper); }
  .contact-item { margin-bottom: 14px; }
  .contact-icon { display: block; height: 18px; }
  .contact-icon svg { width: 20px; height: 18px; fill: var(--paper); }
  .contact-rule { border-top: 1.5px solid var(--rule); margin: 4px 0 8px; }
  .contact-text { font-size: 13.5px; line-height: 21px; }
</style>
</head>
<body>

<section class="card card-front">
  <div class="red-band"></div>
  <div class="brand"><span class="brand-dot"></span>SAFENEST</div>
  <div class="ribbon">www.safenestcloud.com</div>
  <span class="ribbon-fold fold-left"></span>
  <span class="ribbon-fold fold-right"></span>
</section>

<section class="card card-back">
  <div class="faint-mark"></div>
  <ul class="contact-list">
    <li class="contact-item">
      <span class="contact-icon"><svg viewBox="0 0 20 18"><path d="M10 1 L1 9 H4 V17 H8 V12 H12 V17 H16 V9 H19 Z"/></svg></span>
      <div class="contact-rule"></div>
      <p class="contact-text">777 Street Name,<br>Country 54321</p>
    </li>
    <li class="contact-item">
      <span class="contact-icon"><svg viewBox="0 0 20 18"><path d="M2 6 C2 2 18 2 18 6 V8 H14 V6 H6 V8 H2 Z M5 9 H15 L17 16 H3 Z"/><circle cx="10" cy="12.5" r="2" fill="#333334"/></svg></span>
      <div class="contact-rule"></div>
      <p class="contact-text">+000 1234 5678<br>+000 1234 5679</p>
    </li>
    <li class="contact-item">
      <span class="contact-icon"><svg viewBox="0 0 20 18"><path d="M1 1 H19 V13 H12 V15 H15 V17 H5 V15 H8 V13 H1 Z M3 3 V11 H17 V3 Z"/></svg></span>
      <div class="contact-rule"></div>
      <p class="contact-text">info@yourweb.com<br>www.yourweb.com</p>
    </li>
  </ul>
  <div class="red-band"></div>
  <div class="brand"><span class="brand-dot"></span>SAFENEST</div>
  <div class="ribbon">Name</div>
  <span class="ribbon-fold fold-left"></span>
  <p class="designation">Designation</p>
</section>

</body>
</html>
```